Birchford Realty Business Card

Business Card:

Somewhere on front of card, please include Broker License Number: 5839162

Website is BirchfordRealty.example

Address is:
7218 Crestover Ave E
Saginaw, MI 48271

I'll let you use creative freedom on the rest; we obviously need Name, Title, Email (@BirchfordRealty.example), Office Phone, Cell Phone.

Don't want any special die-cutting, just a standard size business card.

On the back, include a place for the date and time of an appointment to be written in pen.

Requirements
Must have
• Our logo, attached to email.

```html
<!DOCTYPE html>
<html lang="en">
<head>
<meta charset="utf-8">
<title>Birchford Realty Business Card</title>
<link href="https://fonts.googleapis.com/css2?family=Open+Sans:wght@400;600;700&display=swap" rel="stylesheet">
<style>
  :root {
    --navy: #25277a;
    --band-edge: #c9cae6;
    --ink: #3f3f3f;
    --muted: #a3a3a3;
    --rule: #6b6b7a;
    --card: #fbfbfb;
    --backdrop: #3b3b3b;
  }
  * { box-sizing: border-box; margin: 0; padding: 0; }
  html, body {
    width: 1200px; height: 750px; overflow: hidden;
    background: var(--backdrop);
    font-family: "Open Sans", Arial, sans-serif;
  }
  .card {
    position: absolute; top: 228px;
    width: 461px; height: 263px;
    background: var(--card);
    overflow: hidden;
  }
  .card--front { left: 124px; }
  .card--back { left: 618px; }

  /* Front */
  .side-band { position: absolute; left: 0; top: 0; width: 18px; height: 100%; background: var(--navy); }
  .side-band-edge { position: absolute; left: 19px; top: 0; width: 2px; height: 100%; background: var(--band-edge); }
  .wordmark {
    position: absolute; left: 38px; top: 58px;
    font-weight: 700; font-size: 24px; color: var(--navy); letter-spacing: -0.2px;
  }
  .person { position: absolute; right: 25px; top: 43px; text-align: right; }
  .person-name { font-weight: 600; font-size: 17px; color: var(--navy); line-height: 22px; }
  .person-title { font-size: 12.5px; color: var(--muted); line-height: 17px; }
  .name-tab { position: absolute; left: 446px; top: 46px; width: 15px; height: 34px; background: var(--navy); }
  .address { position: absolute; left: 38px; top: 137px; font-size: 11px; line-height: 14.5px; color: var(--ink); }
  .contacts { position: absolute; left: 38px; top: 175px; list-style: none; }
  .contacts li { display: flex; align-items: center; height: 17.7px; font-size: 11px; color: var(--ink); }
  .contacts svg { width: 11px; height: 11px; margin-right: 8px; fill: var(--navy); flex: none; }
  .license { position: absolute; right: 26px; top: 228px; font-size: 11px; color: var(--ink); }

  /* Back */
  .field-label { position: absolute; font-size: 13px; color: var(--navy); }
  .field-label--date { left: 30px; top: 44px; }
  .field-label--time { left: 259px; top: 43px; }
  .ampm { position: absolute; right: 31px; top: 50px; font-size: 9.5px; color: var(--navy); }
  .rule { position: absolute; height: 1px; background: var(--rule); }
  .wordmark--back { left: auto; right: 31px; top: 188px; font-size: 19px; }
</style>
</head>
<body>

<section class="card card--front" aria-label="Card front">
  <div class="side-band"></div>
  <div class="side-band-edge"></div>
  <div class="wordmark">Birchford Realty</div>

  <div class="person">
    <div class="person-name">Dana Whitlow</div>
    <div class="person-title">CEO/Founder</div>
  </div>
  <div class="name-tab"></div>

  <address class="address" style="font-style:normal">
    7218 Crestover Ave E<br>Saginaw, MI 48271
  </address>

  <ul class="contacts">
    <li>
      <svg viewBox="0 0 24 24"><path d="M6.6 10.8a15.1 15.1 0 0 0 6.6 6.6l2.2-2.2a1 1 0 0 1 1-.25 11.4 11.4 0 0 0 3.6.57 1 1 0 0 1 1 1V20a1 1 0 0 1-1 1A17 17 0 0 1 3 4a1 1 0 0 1 1-1h3.5a1 1 0 0 1 1 1c0 1.25.2 2.45.57 3.57a1 1 0 0 1-.25 1z"/></svg>
      555 214 7390
    </li>
    <li>
      <svg viewBox="0 0 24 24"><path d="M7 1h10a2 2 0 0 1 2 2v18a2 2 0 0 1-2 2H7a2 2 0 0 1-2-2V3a2 2 0 0 1 2-2zm0 3v14h10V4zm5 15.5a1 1 0 1 0 0 2 1 1 0 0 0 0-2z"/></svg>
      555 862 1047
    </li>
    <li>
      <svg viewBox="0 0 24 24"><path d="M2 5h20v14H2zm2 2v.4l8 5 8-5V7zm0 2.8V17h16V9.8l-8 5z"/></svg>
      name@BirchfordRealty.example
    </li>
    <li>
      <svg viewBox="0 0 24 24"><path d="M12 2a10 10 0 1 0 0 20 10 10 0 0 0 0-20zm-1 17.9A8 8 0 0 1 4.2 10.6L9 15.4v1a2 2 0 0 0 2 2zm6.9-2.5A2 2 0 0 0 16 16h-1v-3a1 1 0 0 0-1-1H8v-2h2a1 1 0 0 0 1-1V7h2a2 2 0 0 0 2-2v-.4a8 8 0 0 1 2.9 12.8z"/></svg>
      www.BirchfordRealty.example
    </li>
  </ul>

  <div class="license">Broker Lic No: 5839162</div>
</section>

<section class="card card--back" aria-label="Card back">
  <div class="field-label field-label--date">Date :</div>
  <div class="rule" style="left:31px; top:63px; width:212px;"></div>
  <div class="field-label field-label--time">Time :</div>
  <div class="ampm">AM/PM</div>
  <div class="rule" style="left:262px; top:63px; width:168px;"></div>

  <div class="rule" style="left:34px; top:100px; width:396px;"></div>
  <div class="rule" style="left:34px; top:138px; width:396px;"></div>
  <div class="rule" style="left:34px; top:168px; width:325px;"></div>
  <div class="rule" style="left:34px; top:202px; width:229px;"></div>
  <div class="rule" style="left:34px; top:235px; width:334px;"></div>

  <div class="wordmark wordmark--back">Birchford Realty</div>
</section>

</body>
</html>
```